KOVlane stands for Kestrel & Ordway venture technologies and specialises in process automation

We are a New company called KOVlane (Kestrel & Ordway venture technologies) a Brisbane based company speciallising in Process Automation for the oil and Gas industry in Australia. We work on projects for DCS, RTU and PLC automation this involves programming and commissioning. We initially need a Website that customers can see about the company and make enquiries. We currently have Royal Blue and grey as our colours on our email signatures but are open for suggestions. Keywords i would suggest yo to look at for insperation are CSG ( coalseam gas) DCS (Distributed control system) RTU (remote terminal unit) and PLC (programmable logic controller).

Target Market(s)

Large CSG companies in Australia, Marlow, Telmar, WXJ, Bendle

Industry/Entity Type

Industry

```html
<!DOCTYPE html>
<html lang="en">
<head>
<meta charset="utf-8">
<title>KOVlane – Kestrel &amp; Ordway venture technologies</title>
<link href="https://fonts.googleapis.com/css2?family=Arimo:wght@400;700&family=Russo+One&family=Saira+Condensed:wght@500;800&display=swap" rel="stylesheet">
<style>
:root{
  --royal:#1b2a8c;
  --grey-bg:#efefef;
  --grey-card:#f3f3f3;
  --text:#333;
  --muted:#777;
  --line:#c9c9c9;
  --field:#dcdcdc;
  --btn:#9a9a9a;
  --foot-title:#555;
  --white:#fff;
}
*{margin:0;padding:0;box-sizing:border-box}
html,body{width:794px;height:1200px;overflow:hidden}
body{position:relative;background:var(--white);font-family:"Arimo",Arial,sans-serif;color:var(--text);font-size:9.5px;line-height:1.3}
.abs{position:absolute}
.display{font-family:"Saira Condensed",sans-serif;font-weight:800;color:var(--royal);line-height:1;text-transform:uppercase;white-space:nowrap}

/* header */
.brand{left:15px;top:18px;display:flex;align-items:center;gap:6px}
.brand-mark{width:14px;height:14px;background:var(--royal)}
.brand-name{font-family:"Russo One",sans-serif;font-size:32px;color:var(--royal);line-height:1}
.brand-tag{left:32px;top:55px;font-size:8.5px;color:var(--muted)}
.util{right:11px;top:22px;font-size:8px;color:#444}
.search{left:570px;top:41px;width:217px;height:23px;border-radius:12px;background:#e4e4e4;border:1px solid #d4d4d4;padding:5px 11px;font-size:9.5px;color:#555}
.search-btn{position:absolute;right:3px;top:2px;width:25px;height:17px;border-radius:8px;background:#9d9d9d}

/* nav */
.nav{left:0;top:79px;width:794px;height:31px;background:var(--royal)}
.nav a{position:absolute;top:7px;font-family:"Saira Condensed",sans-serif;font-weight:500;font-size:12px;color:var(--white);text-decoration:none;letter-spacing:.6px;text-transform:uppercase}

/* hero */
.hero{left:0;top:110px;width:794px;height:289px;background:linear-gradient(180deg,#8a8a8c 0%,#b9b5b4 35%,#c74a48 55%,#9a9898 80%,#6f6f70 100%)}

/* feature band */
.band{left:0;top:399px;width:794px;height:264px;background:var(--grey-bg)}
.card{top:375px;width:239px;height:270px;background:linear-gradient(180deg,var(--grey-card) 0%,var(--grey-bg) 60%);border-radius:5px 5px 0 0}
.card h2{font-size:16px;text-align:center;margin-top:14px;letter-spacing:.1px}
.card .photo{position:absolute;left:20px;top:44px;width:190px;height:114px;border:2px solid #c8c8c8}
.card p{position:absolute;left:12px;top:169px;width:225px;font-size:9.2px;color:#222;line-height:1.28}
.btn{position:absolute;left:12px;top:212px;width:63px;height:19px;border:2px solid #333;background:var(--white);font-size:8px;font-weight:700;text-align:center;line-height:15px;color:#333}

/* info section */
.sec-title{font-size:34px;top:702px}
.testimonial{left:22px;width:302px;font-size:9.3px;color:#333}
.by{color:var(--royal);font-weight:700;font-size:9.3px;left:22px}
.rule{left:20px;top:827px;width:299px;height:1px;background:var(--line)}
.list{list-style:none;font-size:9.3px;color:#444}
.list li{position:relative;padding-left:12px;height:16.2px}
.list li::before{content:"";position:absolute;left:1px;top:3px;width:4px;height:4px;border:1.6px solid #555;border-radius:50%}

/* footer */
.footer{left:0;top:958px;width:794px;height:242px;background:var(--grey-bg)}
.foot-title{font-size:21px;color:var(--foot-title);top:996px}
.foot-links{font-size:9.3px;color:#888;line-height:11.8px}
.field{left:272px;width:207px;height:21px;border:1px solid #ccc;border-radius:4px;background:var(--field);font-size:9.5px;font-weight:700;color:#555;padding:4px 11px}
.send{left:414px;top:1147px;width:63px;height:19px;background:var(--btn);border:2px solid #ccc;color:var(--white);font-size:8.5px;font-weight:700;text-align:center;line-height:15px}
.contact{left:562px;top:1030px;font-size:9.3px;color:#333;line-height:11.8px;font-style:normal}
.social{left:560px;top:1086px;display:flex;gap:8px}
.social span{width:22px;height:22px;border-radius:50%;background:#9c9c9c}
</style>
</head>
<body>

<header>
  <div class="abs brand"><span class="brand-mark"></span><span class="brand-name">KOVlane</span></div>
  <div class="abs brand-tag">Kestrel &amp; Ordway venture technologies</div>
  <div class="abs util">home · sitemap · careers · contact</div>
  <div class="abs search">Search<span class="search-btn"></span></div>
</header>

<nav class="abs nav">
  <a style="left:18px">Home</a>
  <a style="left:70px">About</a>
  <a style="left:125px">Services</a>
  <a style="left:193px">Solutions</a>
  <a style="left:267px">Clients</a>
  <a style="left:330px">Experiences</a>
  <a style="left:414px">Latest News</a>
  <a style="left:503px">Contact Us</a>
</nav>

<div class="abs hero" role="img" aria-label="Photo of an automated bottling line with a red rotary filling table"></div>

<div class="abs band"></div>

<article class="abs card" style="left:12px">
  <h2 class="display">Distributed Control System</h2>
  <div class="photo" role="img" aria-label="Photo of filling nozzles over bottles on a production line" style="background:linear-gradient(135deg,#cfcfd2,#8e8e95 60%,#4b4f66)"></div>
  <p>Lorem ipsum dolor sit amet, consectetur adipisicing elit, sed do eiusmod tempor incididunt ut labore et dolore magna aliqua. Ut enim ad minim .</p>
  <div class="btn">INQUIRE</div>
</article>

<article class="abs card" style="left:275px">
  <h2 class="display">Remote Terminal Unit</h2>
  <div class="photo" role="img" aria-label="Photo of a control panel with switches and indicator lights" style="background:linear-gradient(160deg,#dfe6e4,#c5cfcc 60%,#a9b3b1)"></div>
  <p>Lorem ipsum dolor sit amet, consectetur adipisicing elit, sed do eiusmod tempor incididunt ut labore et dolore magna aliqua. Ut enim ad minim .</p>
  <div class="btn">INQUIRE</div>
</article>

<article class="abs card" style="left:539px">
  <h2 class="display">Programmable Logic Controller</h2>
  <div class="photo" role="img" aria-label="Photo of a control room desk with monitors showing process screens" style="background:linear-gradient(160deg,#e8e8ec,#a9b6d6 50%,#d3d3d6)"></div>
  <p>Lorem ipsum dolor sit amet, consectetur adipisicing elit, sed do eiusmod tempor incididunt ut labore et dolore magna aliqua. Ut enim ad minim .</p>
  <div class="btn">INQUIRE</div>
</article>

<section>
  <h2 class="abs display sec-title" style="left:20px">Testimonials</h2>
  <p class="abs testimonial" style="top:748px">At vero eos et accusamus et iusto odio dignissimos ducimus, qui blanditiis praesentium voluptatum deleniti atque corrupti, quos dolores et quas molestias excepturi sint, obcaecati cupiditate non provident, similique sunt in culpa, qui officia deserunt mollitia animi, id est</p>
  <p class="abs by" style="top:800px">by: oil industry name</p>
  <div class="abs rule"></div>
  <p class="abs testimonial" style="top:845px">Temporibus autem quibusdam et aut officiis debitis aut rerum necessitatibus saepe eveniet, ut et voluptates repudiandae sint et molestiae non recusandae. Itaque earum rerum hic tenetur a sapiente delectus, ut aut reiciendis voluptatibus maiores alias consequatur.</p>
  <p class="abs by" style="top:896px">by: another client</p>

  <h2 class="abs display sec-title" style="left:383px">Services</h2>
  <ul class="abs list" style="left:392px;top:747px">
    <li>Consulting &amp; Design</li>
    <li>Project Management</li>
    <li>Engineering Services</li>
    <li>Solutions</li>
    <li>PLC / PAC / RTU</li>
    <li>SCADA / HMI</li>
    <li>Industrial Networking &amp; IT</li>
    <li>Business Intelligence</li>
    <li>Onsite Services, Support &amp; Training</li>
  </ul>

  <h2 class="abs display sec-title" style="left:602px">Solutions</h2>
  <ul class="abs list" style="left:611px;top:747px">
    <li>Mining</li>
    <li>Oil &amp; Gas</li>
    <li>Water</li>
    <li>Food &amp; Beverage</li>
    <li>Manufacturing</li>
    <li>Commercial</li>
  </ul>
</section>

<footer>
  <div class="abs footer"></div>
  <h2 class="abs display foot-title" style="left:20px">Navigation</h2>
  <div class="abs foot-links" style="left:21px;top:1032px">Home<br>About<br>Services<br>Solutions<br>Clients<br>Experiences</div>
  <div class="abs foot-links" style="left:103px;top:1032px">Sitemap<br>Latest News<br>Privacy Policy<br>Terms of Use<br>Contact Us</div>

  <h2 class="abs display foot-title" style="left:274px">Inquire Now</h2>
  <div class="abs field" style="top:1030px">full name</div>
  <div class="abs field" style="top:1054px">email</div>
  <div class="abs field" style="top:1077px;height:60px">inquries</div>
  <div class="abs send">INQUIRE</div>

  <h2 class="abs display foot-title" style="left:561px">Contact Us</h2>
  <address class="abs contact">Level 2, 48 Harrowfield Lane<br>Westbrook QLD 4102<br>Ph: +61-27-31940 0155 / Fax: +61-27-31940 0156<br>Email: sales@kovlane.com.au</address>
  <div class="abs social" aria-label="Social links"><span></span><span></span><span></span><span></span><span></span></div>
</footer>

</body>
</html>
```